1887 Basins & Spouts Business Card

I'm wanting to get a business card designed. Our business is 1887 Basins & Spouts
Details for the card:

1887 Basins & Spouts
Name: Warren Tobbit
Email: warren@1887basinsandspouts.com.au
Website: www.1887basinsandspouts.com.au
Mobile: 0438 169 204
Phone: 02 6187 4932

Font of Basins & Spouts is called Snell Roundhand. Not sue what font logo text is.

I'm thinking two sided but it doesn't have to be.

```html
<!DOCTYPE html>
<html lang="en">
<head>
<meta charset="utf-8">
<title>1887 Basins &amp; Spouts – Business Card</title>
<link rel="stylesheet" href="https://fonts.googleapis.com/css2?family=Montserrat:wght@400;500;600&family=Open+Sans:wght@600&family=Pinyon+Script&display=swap">
<style>
  :root {
    --backdrop: #2b2b2b;
    --card: #ffffff;
    --ink: #141414;
    --ink-soft: #3a3a3a;
    --rule: #222222;
  }
  * { box-sizing: border-box; margin: 0; padding: 0; }
  html, body { width: 1200px; height: 900px; overflow: hidden; }
  body {
    background: var(--backdrop);
    position: relative;
    font-family: "Montserrat", sans-serif;
    color: var(--ink);
  }
  .card {
    position: absolute;
    width: 580px;
    height: 340px;
    background: var(--card);
    border-radius: 26px;
  }
  .card--front { left: 120px; top: 70px; }
  .card--back { left: 500px; top: 490px; }

  /* front */
  .front-brand {
    position: absolute;
    left: 0; right: 0; top: 122px;
    display: flex; align-items: center; justify-content: center; gap: 14px;
  }
  .brand-mark {
    width: 16px; height: 16px; border-radius: 50%;
    background: var(--ink);
    flex: none;
  }
  .brand-name {
    font-family: "Montserrat", sans-serif;
    font-weight: 500;
    font-size: 34px;
    letter-spacing: 1px;
    color: var(--ink);
  }
  .tagline {
    position: absolute;
    left: 0; right: 0; top: 200px;
    text-align: center;
    font-family: "Open Sans", sans-serif;
    font-weight: 600;
    font-size: 14px;
    color: var(--ink);
  }

  /* back */
  .back-brand {
    position: absolute;
    left: 30px; width: 190px; top: 0; bottom: 0;
    display: flex; flex-direction: column; align-items: center; justify-content: center; gap: 10px;
    text-align: center;
  }
  .back-brand .brand-name { font-size: 24px; line-height: 1.25; }
  .divider {
    position: absolute;
    left: 250px; top: 70px;
    width: 1.5px; height: 200px;
    background: var(--rule);
  }
  .contact {
    position: absolute;
    left: 278px; top: 86px; right: 16px;
  }
  .contact-name {
    font-family: "Pinyon Script", cursive;
    font-weight: 400;
    font-size: 36px;
    line-height: 1;
    color: var(--ink);
  }
  .contact-role {
    font-size: 13px;
    color: var(--ink-soft);
    margin-bottom: 12px;
  }
  .contact-list { list-style: none; font-size: 12.5px; line-height: 1.55; }
  .contact-list b { font-weight: 600; display: inline-block; width: 16px; }
</style>
</head>
<body>
  <section class="card card--front" aria-label="Card front">
    <div class="front-brand">
      <span class="brand-mark"></span>
      <span class="brand-name">1887 Basins &amp; Spouts</span>
    </div>
    <p class="tagline">Classic craftsmanship made for the way you live today</p>
  </section>

  <section class="card card--back" aria-label="Card back">
    <div class="back-brand">
      <span class="brand-mark"></span>
      <span class="brand-name">1887 Basins<br>&amp; Spouts</span>
    </div>
    <div class="divider"></div>
    <div class="contact">
      <h1 class="contact-name">Warren Tobbit</h1>
      <p class="contact-role">managing director</p>
      <ul class="contact-list">
        <li><b>m</b>0438 169 204</li>
        <li><b>p</b>02 6187 4932</li>
        <li><b>e</b>warren@1887basinsandspouts.com.au</li>
        <li><b>w</b>www.1887basinsandspouts.com.au</li>
      </ul>
    </div>
  </section>
</body>
</html>
```